residential roofing company needs a Truck wrap design.

We need a Van wrap design. We are a local residential roofing contractor.That specialize in Roofing Eavestrough and siding we need a design that will stand out and look professional.We really want roofing to stand out as that's our main focus. We like a clean a simple and modern design. Our website is www.larkfieldexteriors.ca The van we are wrapping is a 2019 Halvorsen-Kraft Tolvane 2500 Cargo 170 WB High Roof. We want to incorporate our phone number 844 612 DECK

```html
<!DOCTYPE html>
<html lang="en">
<head>
<meta charset="utf-8">
<title>Larkfield Exteriors – Van Wrap</title>
<link rel="stylesheet" href="https://fonts.googleapis.com/css2?family=Archivo:wght@700&family=Montserrat:wght@600&family=Saira+Semi+Condensed:wght@600&display=swap">
<style>
  :root {
    --bg: #ffffff;
    --van-light: #f7f7f7;
    --van-dark: #4b4b4b;
    --band-light: #2f2f2f;
    --band-dark: #3a3a3a;
    --trim: #262626;
    --glass: #3d3d3d;
    --tyre: #1e1e1e;
    --hub: #8a8a8a;
    --tail: #b3121b;
    --brand-yellow: #eca91b;
    --ink-grey: #555555;
    --ink-white: #f3f3f3;
    --panel-line: rgba(0,0,0,0.12);
  }
  html, body {
    margin: 0;
    padding: 0;
    width: 906px;
    height: 1200px;
    overflow: hidden;
    background: var(--bg);
  }
  .wrap-sheet { display: block; width: 906px; height: 1200px; }
  .van-body--light { fill: var(--van-light); stroke: #d8d8d8; stroke-width: 2; }
  .van-body--dark { fill: var(--van-dark); }
  .panel-seam { stroke: var(--panel-line); stroke-width: 3; fill: none; }
  .rub-strip--light { fill: var(--band-light); }
  .rub-strip--dark { fill: var(--band-dark); }
  .front-bumper { fill: var(--trim); }
  .cab-window { fill: var(--glass); }
  .tail-light { fill: var(--tail); }
  .tyre { fill: var(--tyre); }
  .hub { fill: var(--hub); stroke: #5a5a5a; stroke-width: 6; }
  .brand-square { fill: var(--brand-yellow); }
  .brand-name {
    font-family: "Archivo", Arial, sans-serif;
    font-weight: 700;
  }
  .brand-name--line1 { font-size: 118px; }
  .brand-name--line2 { font-size: 62px; }
  .tagline {
    font-family: "Montserrat", Arial, sans-serif;
    font-weight: 600;
    font-size: 32px;
  }
  .phone {
    font-family: "Saira Semi Condensed", Arial Narrow, sans-serif;
    font-weight: 600;
    font-size: 96px;
  }
  .ink--grey { fill: var(--ink-grey); }
  .ink--white { fill: var(--ink-white); }
</style>
</head>
<body>
<svg class="wrap-sheet" viewBox="0 0 1680 2222" xmlns="http://www.w3.org/2000/svg">
  <defs>
    <path id="van-outline" d="M 60 670 C 70 640 150 600 240 585 L 420 360 C 450 340 500 330 550 325 L 1520 300 C 1550 300 1560 320 1565 360 L 1605 720 L 1605 790 L 1628 800 L 1628 815 L 1560 830 L 1345 838 A 100 100 0 0 0 1150 840 L 325 860 A 100 100 0 0 0 135 862 L 45 850 L 40 760 Z"/>
  </defs>

  <!-- White van -->
  <g class="van van--white">
    <use href="#van-outline" class="van-body--light"/>
    <path class="panel-seam" d="M 550 325 L 555 840 M 900 318 L 915 838 M 525 420 L 520 845"/>
    <rect class="rub-strip--light" x="315" y="732" width="1250" height="58"/>
    <path class="front-bumper" d="M 40 760 L 60 700 L 300 700 L 330 790 L 330 860 L 135 862 L 45 850 Z"/>
    <path class="cab-window" d="M 300 540 L 385 440 L 515 436 L 518 598 L 300 622 Z"/>
    <rect class="tail-light" x="1567" y="580" width="38" height="135"/>
    <circle class="tyre" cx="230" cy="858" r="90"/>
    <circle class="hub" cx="230" cy="858" r="48"/>
    <circle class="tyre" cx="1248" cy="848" r="90"/>
    <circle class="hub" cx="1248" cy="848" r="48"/>

    <rect class="brand-square" x="578" y="380" width="300" height="300"/>
    <text class="brand-name brand-name--line1 ink--grey" x="945" y="478" textLength="555" lengthAdjust="spacingAndGlyphs">LARKFIELD</text>
    <text class="brand-name brand-name--line2 ink--grey" x="948" y="542" textLength="555" lengthAdjust="spacingAndGlyphs">EXTERIORS.ca</text>
    <text class="tagline ink--grey" x="950" y="578" textLength="553" lengthAdjust="spacing">ROOFING &amp; EXTERIORS</text>
    <text class="phone ink--grey" x="955" y="665" textLength="530" lengthAdjust="spacingAndGlyphs">844 612 DECK</text>
  </g>

  <!-- Charcoal van -->
  <g class="van van--charcoal" transform="translate(0 960)">
    <use href="#van-outline" class="van-body--dark"/>
    <path class="panel-seam" d="M 550 325 L 555 840 M 900 318 L 915 838 M 525 420 L 520 845"/>
    <rect class="rub-strip--dark" x="315" y="732" width="1250" height="58"/>
    <path class="front-bumper" d="M 40 760 L 60 700 L 300 700 L 330 790 L 330 860 L 135 862 L 45 850 Z"/>
    <path class="cab-window" d="M 300 540 L 385 440 L 515 436 L 518 598 L 300 622 Z"/>
    <rect class="tail-light" x="1567" y="580" width="38" height="135"/>
    <circle class="tyre" cx="230" cy="858" r="90"/>
    <circle class="hub" cx="230" cy="858" r="48"/>
    <circle class="tyre" cx="1248" cy="848" r="90"/>
    <circle class="hub" cx="1248" cy="848" r="48"/>

    <rect class="brand-square" x="578" y="380" width="300" height="300"/>
    <text class="brand-name brand-name--line1 ink--white" x="945" y="478" textLength="555" lengthAdjust="spacingAndGlyphs">LARKFIELD</text>
    <text class="brand-name brand-name--line2 ink--white" x="948" y="542" textLength="555" lengthAdjust="spacingAndGlyphs">EXTERIORS.ca</text>
    <text class="tagline ink--white" x="950" y="578" textLength="553" lengthAdjust="spacing">ROOFING &amp; EXTERIORS</text>
    <text class="phone ink--white" x="955" y="665" textLength="530" lengthAdjust="spacingAndGlyphs">844 612 DECK</text>
  </g>
</svg>
</body>
</html>
```